Real Estate Agent needs business card design

We have logo designed already, want to have business card designed. Very interested in those smaller size business card as they look very trendy. Business name is called VORENDA REALTY

```html
<!DOCTYPE html>
<html lang="en">
<head>
<meta charset="utf-8">
<title>Vorenda Realty – Business Card</title>
<link rel="stylesheet" href="https://fonts.googleapis.com/css2?family=Crimson+Text:ital,wght@0,400;1,400&family=Sorts+Mill+Goudy&display=swap">
<style>
  :root {
    --page-bg: #e4e4e4;
    --gold-light: #b7976a;
    --gold-dark: #a07f55;
    --charcoal: #2d2e30;
    --gold-text: #c49a5c;
    --ivory: #f6f2ea;
    --card-radius: 13px;
  }
  * { margin: 0; padding: 0; box-sizing: border-box; }
  html, body {
    width: 1200px;
    height: 576px;
    overflow: hidden;
    background: var(--page-bg);
  }
  .sheet {
    position: relative;
    width: 1200px;
    height: 576px;
  }
  .card {
    position: absolute;
    top: 138px;
    border-radius: var(--card-radius);
  }
  .card--front {
    left: 81px;
    width: 486px;
    height: 294px;
    background: linear-gradient(180deg, var(--gold-light) 0%, var(--gold-light) 45%, var(--gold-dark) 100%);
  }
  .card--back {
    left: 602px;
    width: 480px;
    height: 291px;
    background: var(--charcoal);
    text-align: center;
    font-family: "Crimson Text", Georgia, serif;
    color: var(--ivory);
  }
  .brand {
    position: absolute;
    left: 0;
    right: 0;
    top: 104px;
    display: flex;
    flex-direction: column;
    align-items: center;
    gap: 22px;
  }
  .brand__mark {
    width: 44px;
    height: 44px;
    background: var(--ivory);
  }
  .brand__name {
    font-family: "Crimson Text", Georgia, serif;
    font-size: 26px;
    font-variant: small-caps;
    letter-spacing: 0.5px;
    color: var(--ivory);
    line-height: 1;
  }
  .agent {
    position: absolute;
    left: 0;
    right: 0;
    top: 82px;
  }
  .agent__name {
    font-family: "Sorts Mill Goudy", Georgia, serif;
    font-size: 23px;
    color: var(--gold-text);
    line-height: 1.15;
  }
  .agent__title {
    font-style: italic;
    font-size: 11.5px;
    line-height: 1.3;
  }
  .contact {
    margin-top: 17px;
    font-size: 13px;
    line-height: 16px;
  }
  .contact__group + .contact__group { margin-top: 6px; }
  .contact__highlight { color: var(--gold-text); }
</style>
</head>
<body>
  <main class="sheet">
    <section class="card card--front" aria-label="Card front">
      <div class="brand">
        <span class="brand__mark" aria-hidden="true"></span>
        <span class="brand__name">Vorenda Realty</span>
      </div>
    </section>

    <section class="card card--back" aria-label="Card back">
      <div class="agent">
        <p class="agent__name">Hannah Lorimer</p>
        <p class="agent__title">Senior Property Consultant</p>
        <div class="contact">
          <p class="contact__group">4A, 318 Kestrel Avenue,<br>North Sydney, NSW 2060</p>
          <p class="contact__group">0491 570 156<br>www.<span class="contact__highlight">vorendarealty</span>.com.au</p>
        </div>
      </div>
    </section>
  </main>
</body>
</html>
```